Motivational Quotes Poster Series

This is a 3 poster design series for Ridgeway Haul Academy. The size of each poster should be 18 inches wide and 24 inches tall. The goal of these posters is to serve as motivational "signs" to be hung in the office area for the employees (not customers). These employees are instructors/teachers, teaching students how to drive semi trucks. While each design is a separate poster and design, we're posting as 1 project because we'd like some continuity between the series. Below we'll break down the details of all 3 posters...

Poster #1
Text that must appear on poster - "If You Want The Best Out Of Each Student" and "Give The Best Of You!" Note: While this text must appear on the poster, you can arrange in the layout as you see fit. For example, first line could be at top of poster and second line on bottom.

Poster #2
Text that must appear on poster - "Invest In People" and "Change Someone's Life" (same notes apply as in 1st poster)

Poster #3
Text that must appear on poster - "Today Is..." and "Just Another Day For You" and "The Most Important Day In Their Life" Note: This can be laid out on the poster however you see fit, but each phrase needs to be separate and it needs to flow.

Target Market(s)

Truck Driver Training Instructors - These are middle-aged, mostly male, masculine type personalities.

Industry/Entity Type

Training

Requirements
Must have
• Must have noted text from description
Must have working files (ie - PSD, EPS, AI, etc) provided
Must have common theme between each poster in series
Must have easy to read font and layout
Must have product dimensions of 18 inches (width) by 24 inches (height). If design uses full dimensions please include quarter inch bleed.
Nice to have
• Nice to have a trucking theme...related to trucking industry, but not over the top. Example - This could mean subtle injection of background tire tracks, but by no means are tire tracks required.

For inspiration, you can visit the site at http://www.ridgewayhaulacademy.com. While you can use the colors of the site/logo, you can still branch out between each poster to try new colors within reason.

Note: While we've attached the logo to this project, it COULD be used but doesn't HAVE to be included in the design. The logo IS NOT a focal point. The phrases in the poster ARE the focal point.

```html
<!DOCTYPE html>
<html lang="en">
<head>
<meta charset="utf-8">
<title>Ridgeway Haul Academy – Motivational Poster Series</title>
<link rel="stylesheet" href="https://fonts.googleapis.com/css2?family=Alegreya+Sans+SC:wght@800&family=Archivo:wght@700&display=swap">
<style>
  :root {
    --stage: #e6e6e6;
    --paper: #ffffff;
    --ink: #111111;
    --red: #d52a2e;
    --orange: #ff4a1c;
    --navy: #1c1c8a;
    --frame: #222222;
  }
  html, body {
    margin: 0;
    padding: 0;
    overflow: hidden;
  }
  .canvas {
    position: relative;
    width: 1200px;
    height: 1000px;
    background: var(--stage);
    overflow: hidden;
    font-family: "Alegreya Sans SC", "Trebuchet MS", sans-serif;
    font-weight: 800;
    color: var(--ink);
  }
  .tracks {
    position: absolute;
    inset: 0;
  }
  .line {
    position: absolute;
    margin: 0;
    line-height: 1;
    white-space: nowrap;
    transform-origin: left top;
    transform: scaleX(1.4);
  }
  .line--plain {
    font-family: "Archivo", Arial, sans-serif;
    font-weight: 700;
    letter-spacing: -0.5px;
    transform: none;
  }
  .brand {
    position: absolute;
    margin: 0;
    font-size: 13px;
    line-height: 1;
    white-space: nowrap;
    color: var(--ink);
  }
  .accent-orange { color: var(--orange); }
</style>
</head>
<body>
<main class="canvas">

  <svg class="tracks" width="1200" height="1000" viewBox="0 0 1200 1000">
    <rect class="sheet" x="8" y="228" width="382" height="510" fill="var(--paper)" stroke="var(--frame)" stroke-width="2"/>
    <rect class="sheet" x="408" y="228" width="382" height="510" fill="var(--paper)" stroke="var(--frame)" stroke-width="2"/>
    <rect class="sheet" x="808" y="228" width="382" height="510" fill="var(--paper)" stroke="var(--frame)" stroke-width="2"/>

    <g class="tracks-red" fill="var(--red)">
      <polygon points="95,266 150,266 352,368 295,368"/>
      <polygon points="70,380 235,380 235,418 112,418 148,448 124,456 72,400"/>
      <polygon points="170,530 300,484 360,484 225,530"/>
      <polygon points="15,530 58,530 122,590 52,632 15,632 15,618 75,590 15,562"/>
      <polygon points="170,690 300,645 360,645 225,690"/>
    </g>

    <g class="tracks-orange">
      <polygon fill="var(--orange)" points="440,325 500,325 748,446 700,446"/>
      <polygon fill="var(--orange)" points="425,455 538,455 538,477 430,477"/>
      <polygon fill="var(--ink)" points="425,480 470,480 540,535 500,535"/>
      <polygon fill="var(--ink)" points="525,628 690,572 730,572 570,628"/>
    </g>

    <g class="tracks-navy" fill="var(--navy)">
      <polygon points="860,325 915,325 1148,446 1092,446"/>
      <polygon points="970,530 1115,462 1150,462 1010,530"/>
      <polygon points="880,585 960,585 1090,608 960,632 880,632 990,608"/>
    </g>
  </svg>

  <!-- Poster one -->
  <p class="brand" style="left:74px; top:346px;">Ridgeway Haul Academy</p>
  <p class="line" style="left:28px; top:231px; font-size:45px;">If You</p>
  <p class="line" style="left:196px; top:240px; font-size:34px; transform:rotate(36deg) scaleX(1.4);">Want the</p>
  <p class="line line--plain" style="left:238px; top:374px; font-size:56px;">BEST</p>
  <p class="line" style="left:36px; top:443px; font-size:47px;">Out Of Each</p>
  <p class="line" style="left:122px; top:529px; font-size:41px;">Student</p>
  <p class="line" style="left:58px; top:599px; font-size:38px;">Give The Best</p>
  <p class="line" style="left:115px; top:691px; font-size:46px;">Of You!</p>

  <!-- Poster two -->
  <p class="brand" style="left:436px; top:258px;">Ridgeway Haul Academy</p>
  <p class="line" style="left:418px; top:283px; font-size:47px;">Today Is…</p>
  <p class="line" style="left:574px; top:322px; font-size:20px; transform:rotate(31deg) scaleX(1.4);">Just Another Day</p>
  <p class="line" style="left:540px; top:448px; font-size:50px;">For You</p>
  <p class="line accent-orange" style="left:416px; top:540px; font-size:30px;">The Most Important</p>
  <p class="line accent-orange" style="left:513px; top:634px; font-size:42px;">Day In</p>
  <p class="line accent-orange" style="left:470px; top:689px; font-size:41px;">Their Life</p>

  <!-- Poster three -->
  <p class="brand" style="left:838px; top:258px;">Ridgeway Haul Academy</p>
  <p class="line" style="left:820px; top:277px; font-size:53px;">Invest</p>
  <p class="line" style="left:916px; top:438px; font-size:47px;">In People</p>
  <p class="line" style="left:822px; top:521px; font-size:58px;">Change</p>
  <p class="line" style="left:855px; top:623px; font-size:46px;">Someone's</p>
  <p class="line" style="left:946px; top:683px; font-size:46px;">Life</p>

</main>
</body>
</html>
```